Commercial Bakery needs packing design for a Bread Bag.

Brenton's Bakery needs a design for a bread bag to be distributed to grocery stores. We make all kinds of breads and want this packaging to represent our company. We would like the packaging to be black and white with a fun/bubbly modern design. I have attached a few ideas of what I am looking for.
There are 5 different products. Packaging must be the same for each product except for corresponding product name, bar code and nutrional facts.
Product names:
Coconut Cream Bread
Cream Bread
Potato Rolls
Roll ups
Coconut & Raisin Bread

Our products are packaged in a 11” x 8” poly bag.
I will open 5 contracts with whoever’s design I select. I will then provide nutritional facts, barcodes for items once a contract is selected. Thank you!!

Target Market(s)

Grocery stores

Industry/Entity Type

Bakery

Requirements
Must have
• Black and White (off whites are ok)
Should not have
• Color

```html
<!DOCTYPE html>
<html lang="en">
<head>
<meta charset="utf-8">
<title>Brenton's Bakery – Coconut Cream Bread Bag</title>
<link rel="stylesheet" href="https://fonts.googleapis.com/css2?family=Permanent+Marker&display=swap">
<style>
  :root {
    --ink: #0a0a0a;
    --paper: #ffffff;
    --backdrop: #f1f1f1;
  }
  html, body {
    margin: 0;
    padding: 0;
    width: 1200px;
    height: 1200px;
    overflow: hidden;
    background: var(--backdrop);
  }
  .bread-bag {
    position: absolute;
    left: 50px;
    top: 200px;
    width: 1100px;
    height: 800px;
    background: var(--paper);
  }
  .bread-bag__art {
    position: absolute;
    inset: 0;
    width: 100%;
    height: 100%;
    display: block;
  }
  .stripe { fill: var(--ink); }
  .label-frame { fill: var(--ink); }
  .label-field { fill: var(--paper); }
  .bread-bag__label {
    position: absolute;
    left: 0;
    right: 0;
    top: 0;
    height: 100%;
    text-align: center;
    color: var(--ink);
    font-family: "Permanent Marker", cursive;
  }
  .brand-name {
    position: absolute;
    left: 0;
    right: 0;
    top: 262px;
    margin: 0;
    font-size: 50px;
    line-height: 1;
    font-weight: 400;
  }
  .product-flavour {
    position: absolute;
    left: 0;
    right: 0;
    top: 450px;
    margin: 0;
    font-size: 50px;
    line-height: 1;
    letter-spacing: 1px;
  }
  .product-type {
    position: absolute;
    left: 0;
    right: 0;
    top: 498px;
    margin: 0;
    font-size: 104px;
    line-height: 1;
    letter-spacing: 3px;
  }
</style>
</head>
<body>
  <main class="bread-bag">
    <svg class="bread-bag__art" viewBox="0 0 1100 800" aria-hidden="true">
      <g class="stripes">
        <rect class="stripe" x="0" y="0" width="1100" height="55"/>
        <rect class="stripe" x="0" y="123" width="1100" height="57"/>
        <rect class="stripe" x="0" y="244" width="1100" height="57"/>
        <rect class="stripe" x="0" y="365" width="1100" height="58"/>
        <rect class="stripe" x="0" y="485" width="1100" height="62"/>
        <rect class="stripe" x="0" y="607" width="1100" height="62"/>
        <rect class="stripe" x="0" y="737" width="1100" height="63"/>
      </g>
      <rect class="label-frame" x="33" y="112" width="1034" height="576" rx="150"/>
      <rect class="label-field" x="47" y="157" width="1006" height="484" rx="242"/>
    </svg>
    <section class="bread-bag__label">
      <p class="brand-name">Brenton's Bakery</p>
      <h1 class="product-flavour">COCONUT CREAM</h1>
      <h2 class="product-type">BREAD</h2>
    </section>
  </main>
</body>
</html>
```